Tide Harbor Finance Business Cards

Looking for a business card for a new mortgage broking business. Name of the business is Tide Harbor Finance. Purpose of the business is to build trust and strong relationships with clients to then assist them with your mortgage lending needs. Most relationships within the business start off as an enquiry, and then can evolve into a 10+ year relationship, servicing clients from purchasing a new home to then upgrading for their family and even then assisting their children with their first home purchase. Business card should communicate financial security and trust.

Target Market(s)

Targeting professional clients who are looking to build a relationship with a knowledgeable mortgage professional

Industry/Entity Type

Finance - Home Loans

Contact Information for Business Card

Peter Colburn, Director, mobile: 0427 903186, email:peter@tideharborfinance.com.au, website: www.tideharborfinance.com.au

Font styles to use
Sans Serif

Requirements
Must have
• On the front: Must have company logo, contact details as above. On the back: slogan, 'full of choices, free of stress', plus listing services offered: home loans, investment loans, first home buyers, refinancing, car finance

```html
<!DOCTYPE html>
<html lang="en">
<head>
<meta charset="utf-8">
<title>Tide Harbor Finance – Business Cards</title>
<link rel="stylesheet" href="https://fonts.googleapis.com/css2?family=Montserrat:wght@400;500;700;800;900&family=Oswald:wght@600;700&display=swap">
<style>
  :root {
    --navy: #0a5079;
    --orange: #f0a00a;
    --white: #ffffff;
    --stage: #2a2a2a;
    --shadow: rgba(0,0,0,0.55);
  }
  * { box-sizing: border-box; margin: 0; padding: 0; }
  html, body {
    width: 1200px; height: 1015px; overflow: hidden;
    background: var(--stage);
    font-family: "Montserrat", sans-serif;
  }
  .stage { position: relative; width: 1200px; height: 1015px; }
  .card {
    position: absolute; width: 640px; height: 366px; overflow: hidden;
    box-shadow: 0 18px 40px var(--shadow);
  }

  /* Back card */
  .card-back { left: 70px; top: 90px; background: var(--navy); }
  .slogan {
    position: absolute; left: 150px; top: 90px;
    font-weight: 900; font-size: 38px; line-height: 1.08; letter-spacing: 1px;
    text-transform: uppercase;
  }
  .slogan .line-choices { color: var(--orange); display: block; }
  .slogan .line-stress { color: var(--white); display: block; padding-left: 24px; }
  .services-ribbon { position: absolute; left: 0; top: 238px; width: 400px; height: 58px; }
  .services-label {
    position: absolute; left: 90px; top: 248px;
    font-family: "Oswald", sans-serif; font-weight: 700; font-size: 28px;
    color: var(--white); text-transform: uppercase; letter-spacing: 0.5px;
  }
  .service-list {
    position: absolute; left: 410px; top: 180px; list-style: none;
    color: var(--white); font-size: 15px; font-weight: 500; line-height: 25px;
  }
  .service-list li { display: flex; align-items: center; gap: 7px; }
  .service-list li:nth-child(2) { padding-left: 10px; }
  .service-list li:nth-child(3) { padding-left: 20px; }
  .service-list li:nth-child(4) { padding-left: 30px; }
  .service-list li:nth-child(5) { padding-left: 40px; }
  .bullet {
    width: 12px; height: 12px; border-radius: 50%;
    border: 2px solid var(--orange); position: relative; flex: none;
  }
  .bullet::after {
    content: ""; position: absolute; left: 2px; top: 2px;
    width: 4px; height: 4px; background: var(--orange); border-radius: 50%;
  }

  /* Front card */
  .card-front { left: 490px; top: 560px; background: var(--white); }
  .front-art { position: absolute; inset: 0; }
  .brand {
    position: absolute; right: 40px; top: 30px;
    display: flex; align-items: center; gap: 12px;
    color: var(--navy); font-weight: 800; font-size: 26px; line-height: 1.05;
    text-transform: uppercase; letter-spacing: 0.5px;
  }
  .brand-mark { width: 22px; height: 22px; background: var(--orange); flex: none; }
  .person { position: absolute; left: 40px; top: 200px; }
  .person-name {
    color: var(--white); font-size: 24px; font-weight: 400; line-height: 29px;
    letter-spacing: 1px; text-transform: uppercase;
  }
  .person-name strong { font-weight: 800; }
  .person-role { color: var(--orange); font-size: 16px; font-weight: 500; line-height: 20px; }
  .person-rule { width: 76px; height: 2px; background: var(--orange); margin-top: 8px; }
  .contact-list { list-style: none; margin-top: 8px; }
  .contact-list li {
    display: flex; align-items: center; gap: 10px;
    color: var(--white); font-size: 14.5px; line-height: 24px;
  }
  .contact-icon {
    width: 20px; height: 20px; border: 1.5px solid var(--orange); border-radius: 3px;
    display: flex; align-items: center; justify-content: center; flex: none;
  }
  .contact-icon svg { width: 12px; height: 12px; }
</style>
</head>
<body>
<main class="stage">

  <section class="card card-back" aria-label="Back of business card">
    <h1 class="slogan">
      <span class="line-choices">Full of Choices</span>
      <span class="line-stress">Free of Stress</span>
    </h1>
    <svg class="services-ribbon" viewBox="0 0 400 58" aria-hidden="true">
      <polygon points="0,0 370,0 400,29 370,58 0,58" fill="var(--orange)"/>
    </svg>
    <p class="services-label">Services Offered</p>
    <ul class="service-list">
      <li><span class="bullet"></span>Home Loans</li>
      <li><span class="bullet"></span>Investment Loans</li>
      <li><span class="bullet"></span>First Home Buyers</li>
      <li><span class="bullet"></span>Refinancing</li>
      <li><span class="bullet"></span>Car Finance</li>
    </ul>
  </section>

  <section class="card card-front" aria-label="Front of business card">
    <svg class="front-art" viewBox="0 0 640 366" preserveAspectRatio="none" aria-hidden="true">
      <path d="M0,98 C50,120 110,135 170,140 L60,140 C35,130 15,120 0,114 Z" fill="var(--navy)"/>
      <path d="M0,148 C180,215 420,190 640,100 L640,366 L0,366 Z" fill="var(--navy)"/>
      <path d="M0,118 C130,170 330,165 500,130 C340,185 150,195 0,148 Z" fill="var(--white)"/>
      <path d="M0,125 C140,175 330,170 480,138 C330,190 150,198 10,158 L0,154 Z" fill="var(--orange)"/>
    </svg>
    <div class="brand">
      <span class="brand-mark"></span>
      <span>Tide Harbor<br>Finance</span>
    </div>
    <div class="person">
      <p class="person-name"><strong>Peter</strong> Colburn</p>
      <p class="person-role">Director</p>
      <div class="person-rule"></div>
      <ul class="contact-list">
        <li>
          <span class="contact-icon"><svg viewBox="0 0 12 12"><path d="M2.5,1 L4.5,1 L5,3.5 L3.8,4.4 C4.4,5.8 5.4,6.9 7,7.6 L8,6.5 L10.5,7 L10.5,9.5 C6,10 2,6 2.5,1 Z" fill="var(--orange)"/></svg></span>
          0427 903186
        </li>
        <li>
          <span class="contact-icon"><svg viewBox="0 0 12 12"><rect x="1" y="2.5" width="10" height="7" fill="none" stroke="var(--orange)" stroke-width="1.2"/><path d="M1,2.5 L6,6.5 L11,2.5" fill="none" stroke="var(--orange)" stroke-width="1.2"/></svg></span>
          peter@tideharborfinance.com.au
        </li>
        <li>
          <span class="contact-icon"><svg viewBox="0 0 12 12"><circle cx="6" cy="6" r="4.8" fill="none" stroke="var(--orange)" stroke-width="1.1"/><ellipse cx="6" cy="6" rx="2" ry="4.8" fill="none" stroke="var(--orange)" stroke-width="1"/><path d="M1.2,6 H10.8" stroke="var(--orange)" stroke-width="1"/></svg></span>
          www.tideharborfinance.com.au
        </li>
      </ul>
    </div>
  </section>

</main>
</body>
</html>
```